Real Estate For Sale Sign

I need to design a for sale sign. It needs to include The following information
Logo: Attached
Name: Corinne Vasquel,
Company Name: Gilded Harbor Real Estate,
Phone Number: 503-841-2096
BRE Licence Number 04817359 (Can Be small)
Sign size 24x30

I am not sure about including my website but I would like to see options with it. www.gildedharbor-example.com
Updates

Target Market(s)

Potential Buyers or Sellers of Real Estate. Must be easy to read.

Industry/Entity Type

Real Estate

Requirements
Must have
• I want it to feel luxurious and sharp.

```html
<!DOCTYPE html>
<html lang="en">
<head>
<meta charset="utf-8">
<title>Gilded Harbor Real Estate – For Sale Sign</title>
<link rel="stylesheet" href="https://fonts.googleapis.com/css2?family=Cinzel:wght@400;600&family=Open+Sans:wght@400&family=Arimo:wght@400;700&display=swap">
<style>
  :root {
    --backdrop: #161616;
    --face-light: #ffffff;
    --face-shade: #e4e4e4;
    --brand-blue: #0d55a5;
    --rule-grey: #58585a;
    --ink-dark: #3c3c3e;
    --ink-phone: #454547;
    --ink-fine: #111111;
    --ink-white: #ffffff;
  }
  html, body {
    margin: 0;
    padding: 0;
    width: 829px;
    height: 1200px;
    overflow: hidden;
    background: var(--backdrop);
  }
  .canvas {
    position: relative;
    width: 829px;
    height: 1200px;
    display: flex;
    align-items: center;
    justify-content: center;
  }
  .sign-face {
    display: block;
    width: 716px;
    height: 896px;
  }
  .brand-name {
    font-family: "Cinzel", serif;
    font-weight: 600;
    fill: var(--ink-dark);
  }
  .brand-mark { fill: none; stroke: var(--brand-blue); stroke-width: 6; }
  .headline {
    font-family: "Cinzel", serif;
    font-weight: 600;
    fill: var(--ink-white);
  }
  .agent-name {
    font-family: "Cinzel", serif;
    font-weight: 600;
    fill: var(--brand-blue);
  }
  .phone-number {
    font-family: "Open Sans", sans-serif;
    font-weight: 400;
    fill: var(--ink-phone);
  }
  .phone-ring { fill: none; stroke: var(--brand-blue); stroke-width: 2.5; }
  .phone-handset { fill: var(--brand-blue); }
  .licence {
    font-family: "Arimo", sans-serif;
    fill: var(--ink-fine);
  }
  .website {
    font-family: "Arimo", sans-serif;
    fill: var(--ink-fine);
  }
  .website-domain { font-weight: 700; fill: var(--brand-blue); }
  .rule { fill: var(--rule-grey); }
  .banner { fill: var(--brand-blue); }
</style>
</head>
<body>
<main class="canvas">
  <svg class="sign-face" viewBox="0 0 551 689" xmlns="http://www.w3.org/2000/svg" aria-label="Gilded Harbor Real Estate for sale sign">
    <defs>
      <linearGradient id="faceShade" x1="0" y1="0" x2="1" y2="1">
        <stop offset="0" stop-color="var(--face-light)"/>
        <stop offset="1" stop-color="var(--face-shade)"/>
      </linearGradient>
    </defs>

    <rect class="face-panel" x="0" y="0" width="551" height="689" fill="url(#faceShade)"/>

    <g class="brand">
      <circle class="brand-mark" cx="105" cy="115" r="60"/>
      <text class="brand-name" x="365" y="117" font-size="30" text-anchor="middle">Gilded Harbor</text>
      <text class="brand-name" x="365" y="145" font-size="13" letter-spacing="5" text-anchor="middle">REAL ESTATE</text>
    </g>

    <g class="for-sale-band">
      <rect class="rule" x="0" y="234" width="551" height="5"/>
      <rect class="banner" x="0" y="244" width="551" height="106"/>
      <rect class="rule" x="0" y="352" width="551" height="5"/>
      <text class="headline" x="275" y="326" font-size="80" text-anchor="middle">For Sale</text>
    </g>

    <g class="agent">
      <text class="agent-name" x="275" y="452" font-size="35" text-anchor="middle">Corinne Vasquel</text>
      <g class="phone-icon" transform="translate(92 499)">
        <circle class="phone-ring" cx="0" cy="0" r="18"/>
        <path class="phone-handset" d="M-7,-11 q-5,0 -5,6 q2,13 17,18 q6,0 6,-5 l-5,-5 -4,2 q-5,-3 -7,-7 l2,-4 z"/>
      </g>
      <text class="phone-number" x="127" y="515" font-size="44">503-841-2096</text>
    </g>

    <g class="fine-print">
      <text class="licence" x="275" y="597" font-size="13.5" text-anchor="middle">BRE Licence Number 04817359</text>
      <text class="website" x="275" y="636" font-size="22" letter-spacing="1" text-anchor="middle">www.<tspan class="website-domain">gildedharbor-example</tspan>.com</text>
    </g>
  </svg>
</main>
</body>
</html>
```